Quillmoor Farm Organic Flower Farm, Farmer Florist

I am a flower grower and florist, so I do everything from the field to the vase. I want to include my website, phone, email and instagram

```html
<!DOCTYPE html>
<html lang="en">
<head>
<meta charset="utf-8">
<title>Quillmoor Farm – Business Card</title>
<link rel="stylesheet" href="https://fonts.googleapis.com/css2?family=Noto+Serif:ital,wght@0,400;0,600;1,400&display=swap">
<style>
  :root {
    --backdrop: #8b8d8c;
    --paper: #ffffff;
    --wine: #5c2d33;
    --blush: #f28b8f;
    --ink: #3f3d3e;
    --cream: #fbf6f3;
  }
  * { margin: 0; padding: 0; box-sizing: border-box; }
  html, body {
    width: 1188px; height: 1200px; overflow: hidden;
    background: var(--backdrop);
    font-family: "Noto Serif", Georgia, serif;
  }
  .canvas { position: relative; width: 1188px; height: 1200px; }
  .card { position: absolute; left: 245px; width: 696px; height: 386px; }
  .card--front { top: 159px; background: var(--paper); }
  .card--back { top: 627px; background: var(--wine); }

  .brand {
    position: absolute; left: 0; display: flex; flex-direction: column; align-items: center;
  }
  .card--front .brand { width: 350px; top: 140px; }
  .card--back .brand { width: 696px; top: 110px; }
  .brand__dot { border-radius: 50%; background: var(--blush); }
  .card--front .brand__dot { width: 30px; height: 30px; margin-bottom: 30px; }
  .card--back .brand__dot { width: 42px; height: 42px; margin-bottom: 46px; }
  .brand__name { letter-spacing: 0.08em; line-height: 1; font-weight: 400; }
  .card--front .brand__name { font-size: 31px; color: var(--wine); }
  .card--back .brand__name { font-size: 50px; color: var(--cream); }

  .brand__tagline { font-style: italic; color: var(--blush); line-height: 1; letter-spacing: 0.04em; }
  .card--front .brand__tagline { font-size: 15px; margin-top: 7px; }
  .card--back .brand__tagline { font-size: 24px; margin-top: 11px; }

  .brand__founded { font-weight: 600; letter-spacing: 0.32em; line-height: 1; padding-left: 0.32em; }
  .card--front .brand__founded { font-size: 10px; margin-top: 9px; color: var(--wine); }
  .card--back .brand__founded { font-size: 15px; margin-top: 15px; color: var(--cream); }

  .divider {
    position: absolute; left: 349px; top: 116px; width: 1.5px; height: 154px;
    background: var(--blush);
  }
  .contact { position: absolute; left: 381px; top: 110px; color: var(--ink); }
  .contact__name { font-size: 23px; line-height: 1.1; letter-spacing: 0.01em; }
  .contact__role { font-size: 21px; line-height: 1.1; color: var(--blush); }
  .contact__list { list-style: none; margin-top: 14px; }
  .contact__item {
    display: flex; align-items: center; gap: 7px;
    font-size: 20px; line-height: 25px; height: 25px;
  }
  .contact__icon { width: 18px; height: 18px; flex: none; }
  .contact__icon * { fill: var(--wine); }
</style>
</head>
<body>
<main class="canvas">
  <section class="card card--front" aria-label="Business card front">
    <div class="brand">
      <span class="brand__dot"></span>
      <span class="brand__name">QUILLMOOR</span>
      <span class="brand__tagline">organic flower farm</span>
      <span class="brand__founded">EST. 2019</span>
    </div>
    <span class="divider"></span>
    <div class="contact">
      <p class="contact__name">DANIEL HART</p>
      <p class="contact__role">Owner</p>
      <ul class="contact__list">
        <li class="contact__item">
          <svg class="contact__icon" viewBox="0 0 18 18" aria-hidden="true"><path d="M1 7c0-3 3-4 8-4s8 1 8 4l-4 1-1-2H6L5 8z"/><rect x="4" y="9" width="10" height="6" rx="1"/></svg>
          +56930472619
        </li>
        <li class="contact__item">
          <svg class="contact__icon" viewBox="0 0 18 18" aria-hidden="true"><path d="M1 4h16v10H1z M2.5 5.2 9 10l6.5-4.8V5.5L9 10.3 2.5 5.5z" fill-rule="evenodd"/></svg>
          info@quillmoor.com
        </li>
        <li class="contact__item">
          <svg class="contact__icon" viewBox="0 0 18 18" aria-hidden="true"><circle cx="9" cy="9" r="8"/></svg>
          www.quillmoor.com
        </li>
        <li class="contact__item">
          <svg class="contact__icon" viewBox="0 0 18 18" aria-hidden="true"><rect x="1" y="1" width="16" height="16" rx="2"/></svg>
          @quillmoor
        </li>
      </ul>
    </div>
  </section>

  <section class="card card--back" aria-label="Business card back">
    <div class="brand">
      <span class="brand__dot"></span>
      <span class="brand__name">QUILLMOOR</span>
      <span class="brand__tagline">organic flower farm</span>
      <span class="brand__founded">EST. 2019</span>
    </div>
  </section>
</main>
</body>
</html>
```